Law Firm Website

We are looking to update our old, tired and very flat website. We have someone who will code and host the site but we need some design inspiration. The website will consist of no more than 2/3 pages, possibly with pop-ups for information. We already have all the blurb. We would like something distinctive, clean and eye-catching, using the purple and white theme that we already use on our firm stationery. Examples uploaded. Current website URL is www.dunmorewillett.example.

Industry/Entity Type

Law Firm

```html
<!DOCTYPE html>
<html lang="en">
<head>
<meta charset="utf-8">
<title>Dunmore &amp; Willett Solicitors</title>
<link rel="stylesheet" href="https://fonts.googleapis.com/css2?family=Ubuntu:wght@300;400;500&family=Alfa+Slab+One&display=swap">
<style>
  :root {
    --purple: #5c5698;
    --purple-nav: #5a52a2;
    --purple-line: #6a5fa8;
    --logo-green: #263a2e;
    --white: #ffffff;
    --ink: #222222;
    --footer-ink: #444444;
    --accent-red: #d9202a;
  }
  * { box-sizing: border-box; margin: 0; padding: 0; }
  html, body { width: 1200px; height: 971px; overflow: hidden; background: var(--white); }
  body { position: relative; font-family: "Ubuntu", sans-serif; color: var(--ink); }

  .site-header { position: absolute; left: 0; top: 0; width: 1200px; height: 127px; border-bottom: 3px solid var(--purple-line); }
  .brand { position: absolute; left: 31px; top: 24px; color: var(--logo-green); font-weight: 500; line-height: 1; }
  .brand-name { font-size: 34px; letter-spacing: -0.5px; white-space: nowrap; }
  .brand-sub { font-size: 21px; margin-top: 6px; padding-left: 58px; color: var(--purple-nav); }
  .main-nav { position: absolute; right: 39px; top: 53px; display: flex; gap: 40px; }
  .main-nav a { color: var(--purple-nav); font-weight: 500; font-size: 17px; text-decoration: none; white-space: nowrap; }

  .hero { position: absolute; left: 0; top: 127px; width: 1200px; height: 405px;
    background: linear-gradient(100deg, #e9e9e9 0%, #f6f6f6 40%, #fdfdfd 70%, #f2f2f2 100%); }
  .hero-visual { position: absolute; left: 712px; top: 16px; width: 442px; height: 344px;
    background: radial-gradient(ellipse at 45% 55%, #8a4e2c 0%, #6b3a20 40%, rgba(150,100,70,0.25) 70%, rgba(255,255,255,0) 85%); }
  .hero-card { position: absolute; left: 59px; top: 66px; width: 594px; min-height: 267px; background: var(--purple);
    border-radius: 9px; color: var(--white); padding: 30px 22px 14px; font-weight: 300; font-size: 14.5px; line-height: 20px; }
  .hero-card h1 { font-weight: 400; font-size: 43px; line-height: 1; margin-bottom: 22px; white-space: nowrap; }
  .hero-card p { margin-bottom: 19px; letter-spacing: 0.2px; }
  .hero-card a { color: var(--white); }

  .expertise { position: absolute; left: 0; top: 532px; width: 1200px; height: 283px; background: var(--purple); color: var(--white); }
  .expertise h2 { position: absolute; left: 98px; top: 26px; font-weight: 400; font-size: 35px; }
  .expertise-list { position: absolute; top: 86px; list-style: none; font-weight: 300; font-size: 15px; letter-spacing: 0.3px; }
  .expertise-list li { height: 28.2px; white-space: nowrap; }
  .col-1 { left: 95px; top: 89px; }
  .col-2 { left: 352px; }
  .col-3 { left: 602px; }
  .testimonials { position: absolute; left: 836px; top: 63px; width: 319px; height: 157px; background: #f8f8f8;
    border-radius: 10px; padding: 18px 15px; color: var(--ink); }
  .testimonials h3 { font-weight: 400; font-size: 27px; padding: 0 3px 5px; border-bottom: 1px solid var(--purple); white-space: nowrap; }
  .testimonials p { font-weight: 300; font-size: 14px; line-height: 18px; margin-top: 18px; padding: 0 6px 0 6px; }

  .tagline { position: absolute; left: 0; top: 815px; width: 1200px; height: 90px; border-bottom: 2px solid var(--purple-line);
    display: flex; align-items: center; justify-content: center; white-space: nowrap;
    font-family: "Alfa Slab One", serif; font-size: 30px; color: var(--purple); }

  .site-footer { position: absolute; left: 0; top: 907px; width: 1200px; height: 64px; }
  .footer-nav { position: absolute; left: 28px; top: 17px; display: flex; gap: 47px; }
  .footer-nav a { color: var(--footer-ink); font-weight: 300; font-size: 15px; text-decoration: none; white-space: nowrap; }
  .copyright { position: absolute; left: 28px; top: 42px; font-weight: 300; font-size: 13px; color: var(--ink); }
  .partner { position: absolute; right: 24px; top: 17px; display: flex; align-items: center; gap: 6px;
    font-weight: 400; font-size: 25px; color: var(--footer-ink); }
  .partner-mark { width: 22px; height: 22px; background: var(--accent-red); }
</style>
</head>
<body>
  <header class="site-header">
    <div class="brand">
      <div class="brand-name">Dunmore + Willett</div>
      <div class="brand-sub">Solicitors</div>
    </div>
    <nav class="main-nav">
      <a href="#">Home</a>
      <a href="#">Areas of Expertise</a>
      <a href="#">Edward Dunmore</a>
      <a href="#">Martin Willett</a>
      <a href="#">Contact Us</a>
    </nav>
  </header>

  <section class="hero">
    <div class="hero-visual" role="img" aria-label="Wooden judge's gavel resting on a sound block engraved with the word law"></div>
    <div class="hero-card">
      <h1>Dunmore &amp; Willett Solicitors</h1>
      <p>DUNMORE and WILLETT is a firm of solicitors with offices in Ashcombe, London and Brinley, Hertfordshire. This firm is authorised and regulated by the Legal Standards Authority, no.618305.</p>
      <p>VAT registered number: 731 4092 58</p>
      <p>Professional rules can be viewed on <a href="#">www.legalstandards.example/conduct</a></p>
    </div>
  </section>

  <section class="expertise">
    <h2>Areas of Expertise</h2>
    <ul class="expertise-list col-1">
      <li>Company Matters</li>
      <li>Commercial Matters</li>
      <li>Commercial Crime</li>
      <li>Litigation/Disputes</li>
      <li>Insolvency</li>
      <li>Residential Conveyancing</li>
    </ul>
    <ul class="expertise-list col-2">
      <li>Commercial Conveyancing</li>
      <li>Wills &amp; Probate</li>
      <li>Estate Planning</li>
      <li>powers of Attorney</li>
      <li>Care of the Elderly</li>
      <li>Court of Protection</li>
    </ul>
    <ul class="expertise-list col-3">
      <li>Divorce/Family</li>
      <li>Pre-Nuptial Agreements</li>
      <li>Intellectual Property</li>
      <li>Media Law</li>
    </ul>
    <aside class="testimonials">
      <h3>Client Testimonials</h3>
      <p>"Thank you, thank you, thank you. Your hard work and dedication has changed my life for the better".</p>
    </aside>
  </section>

  <div class="tagline">Dunmore &amp; Willett Solicitors, For The Service Your Deserve</div>

  <footer class="site-footer">
    <nav class="footer-nav">
      <a href="#">Home</a>
      <a href="#">Areas of Expertise</a>
      <a href="#">Edward Dunmore</a>
      <a href="#">Martin Willett</a>
      <a href="#">Contact Us</a>
    </nav>
    <div class="copyright">© 2014 Dunmore+Willett Solicitors. All Rights Reserved.</div>
    <div class="partner"><span class="partner-mark"></span>Accord</div>
  </footer>
</body>
</html>
```